Business Card Design Project

We have a logo design and are now looking for a business card design. We supply pre-construction services to the Wireless Telecommunication Industry in the development of cell phone tower and other antenna supporting infrastructure e.g. buildings. The types of services include Real Estate Leasing, Zoning & Permitting,Surveying and A&E work. I am looking for a card that includes the logo we have selected along with the full company name. Company colors are Blue and Silver. I want something professional and that "pops". Use your imagination with the four sided star portion of the logo - it can be stretched such that it occupies a large portion of the card or kept simple the way it is. I am interested in seeing the design on a white, silver, navy, black or charcoal background or any other color you think works well with the logo. Apart from the logo that includes HRM we also need to see the full company name on the card - Harborline Relay Maintenance, Inc. The design must also show a persons name, title, address, (2) phone numbers, e-mail address and web address www.hrm.example

Target Market(s)

Cell phone carriers e.g. Quellport Mobile, BN&K, Zandex Cell, Ovalo etc.

Industry/Entity Type

Cell Phone

Requirements
Must have
• Logo and
Harborline Relay Maintenance, Inc.

```html
<!DOCTYPE html>
<html lang="en">
<head>
<meta charset="utf-8">
<title>HRM Business Card</title>
<link rel="stylesheet" href="https://fonts.googleapis.com/css2?family=Cinzel:wght@600&family=Open+Sans:wght@400;600;700&display=swap">
<style>
  :root {
    --blue: #1a8fd6;
    --blue-deep: #0f74b8;
    --silver: #c9cdd1;
    --silver-light: #e9ebed;
    --paper: #ffffff;
    --ink: #4a4d50;
    --ink-dark: #2d2f31;
    --stage: #eceef0;
  }
  * { box-sizing: border-box; margin: 0; padding: 0; }
  html, body { width: 1200px; height: 871px; overflow: hidden; }
  body {
    background: var(--stage);
    font-family: "Open Sans", Arial, sans-serif;
    position: relative;
  }
  .card {
    position: absolute;
    width: 560px;
    height: 320px;
    background: var(--paper);
    box-shadow: 0 6px 18px rgba(0,0,0,0.18);
    overflow: hidden;
  }
  /* Front */
  .card-front {
    left: 70px; top: 90px;
    background: linear-gradient(180deg, #ffffff 0%, #f3f4f5 55%, var(--silver-light) 100%);
  }
  .brand {
    position: absolute;
    display: flex;
    align-items: center;
    gap: 16px;
  }
  .brand-dot {
    border-radius: 50%;
    background: var(--blue);
  }
  .brand-name {
    font-family: "Open Sans", Arial, sans-serif;
    font-weight: 700;
    color: var(--blue);
    letter-spacing: 2px;
    line-height: 1;
  }
  .company-name {
    position: absolute;
    font-weight: 600;
    color: var(--ink);
    white-space: nowrap;
    line-height: 1.2;
  }
  .card-front .brand { left: 150px; top: 52px; }
  .card-front .brand-dot { width: 56px; height: 56px; }
  .card-front .brand-name { font-size: 76px; }
  .card-front .company-name {
    left: 0; right: 0; top: 148px;
    text-align: center;
    font-size: 17px;
    letter-spacing: 0.5px;
  }
  .front-band {
    position: absolute;
    left: 0; right: 0; top: 205px;
    height: 44px;
    background: linear-gradient(180deg, var(--blue) 0%, var(--blue-deep) 100%);
    display: flex;
    align-items: center;
    justify-content: center;
  }
  .front-web {
    color: var(--paper);
    font-weight: 600;
    font-size: 17px;
    letter-spacing: 0.5px;
  }
  /* Back */
  .card-back { left: 570px; top: 470px; }
  .card-back .brand { left: 40px; top: 62px; }
  .card-back .brand-dot { width: 40px; height: 40px; }
  .card-back .brand-name { font-size: 58px; }
  .card-back .company-name {
    left: 40px; top: 132px;
    font-size: 12.5px;
  }
  .contact {
    position: absolute;
    left: 318px; top: 52px;
    color: var(--ink);
  }
  .person-name {
    font-family: "Cinzel", Georgia, serif;
    font-weight: 600;
    font-size: 19px;
    color: var(--ink-dark);
    letter-spacing: 0.5px;
  }
  .person-title {
    font-size: 12px;
    font-weight: 600;
    color: var(--blue);
    margin-top: 1px;
  }
  .address {
    font-size: 13px;
    line-height: 18px;
    margin-top: 18px;
  }
  .lines { margin-top: 14px; list-style: none; }
  .lines li {
    display: flex;
    align-items: center;
    font-size: 13px;
    line-height: 18px;
  }
  .lines svg { width: 13px; height: 13px; margin-right: 24px; flex: none; }
  .lines .web { margin-top: 6px; }
  .back-base {
    position: absolute;
    left: 0; bottom: 0;
    width: 560px; height: 90px;
  }
</style>
</head>
<body>

  <section class="card card-front" aria-label="Card front">
    <div class="brand">
      <span class="brand-dot"></span>
      <span class="brand-name">HRM</span>
    </div>
    <p class="company-name">Harborline Relay Maintenance, Inc.</p>
    <div class="front-band">
      <span class="front-web">www.hrm.example</span>
    </div>
  </section>

  <section class="card card-back" aria-label="Card back">
    <div class="brand">
      <span class="brand-dot"></span>
      <span class="brand-name">HRM</span>
    </div>
    <p class="company-name">Harborline Relay Maintenance, Inc.</p>

    <div class="contact">
      <p class="person-name">Dana Whitlock</p>
      <p class="person-title">Ceo</p>
      <p class="address">Level 4, 218 Marrow Street<br>KELDON VALE 4471</p>
      <ul class="lines">
        <li>
          <svg viewBox="0 0 16 16" aria-hidden="true"><path fill="#1a8fd6" d="M2 6c0-2 2-3 6-3s6 1 6 3v1h-3V5.5H5V7H2z"/><rect x="3" y="8" width="10" height="6" rx="1.5" fill="#1a8fd6"/><circle cx="8" cy="11" r="1.5" fill="#fff"/></svg>
          02 5550 0148
        </li>
        <li>
          <svg viewBox="0 0 16 16" aria-hidden="true"><rect x="4" y="1" width="8" height="5" fill="#1a8fd6"/><rect x="1" y="6" width="14" height="6" rx="1" fill="#1a8fd6"/><rect x="4" y="10" width="8" height="5" fill="#fff" stroke="#1a8fd6" stroke-width="1.2"/></svg>
          02 555 0195
        </li>
        <li>
          <svg viewBox="0 0 16 16" aria-hidden="true"><rect x="1" y="3" width="14" height="10" rx="1" fill="#1a8fd6"/><path d="M1.5 3.5 8 9l6.5-5.5" fill="none" stroke="#fff" stroke-width="1.3"/></svg>
          dana.whitlock@hrm.example
        </li>
        <li class="web">www.hrm.example</li>
      </ul>
    </div>

    <svg class="back-base" viewBox="0 0 560 90" aria-hidden="true">
      <defs>
        <linearGradient id="baseSilver" x1="0" y1="0" x2="0" y2="1">
          <stop offset="0" stop-color="#e4e6e8"/>
          <stop offset="1" stop-color="#c9cdd1"/>
        </linearGradient>
      </defs>
      <polygon points="0,40 330,78 560,78 560,90 0,90" fill="#1a8fd6"/>
      <polygon points="0,48 318,84 330,90 0,90" fill="#0f74b8"/>
      <polygon points="318,70 560,70 560,90 340,90" fill="url(#baseSilver)"/>
    </svg>
  </section>

</body>
</html>
```